Personal Injury Funding Flyer

We are Qorva Financial, a provider of receivables management solutions to the surgical industry.
We want a 1 page flyer to showcase our Motor Vehicle Accident (MVA) and Personal Injury (PI) case management and lien purchasing.

1- a flyer from a competitor. We like the overall feel of the flyer and the simplicity of the information presented.

You can also check out our website for examples of our company's style
www.qorvafinancial-example.com

Target Market(s)

Surgeons, office managers, administrators and CFOS at smaller surgical facilities and surgical hospitals nationwide

Industry/Entity Type

Financial

Requirements
Must have
• Titled: Personal Injury Case Funding
• Tagline: We Ensure Your Cases are Financially Sound
• Include Qorva Financial's logo
• Be sure to boldly highlight the 3 points:
• 3 Steps to Successful PI Case Management
• 1) Evaluate Cases
• Evaluate the financial aspects of the case including policy limits.
• 2) Consult Attorneys
• Evaluate the case background and likelihood of settlement.
• 3) Guaranteed Funding
• 15 day funding on most cases.
• How Does MVA/PI Funding Work?
• We pay you upfront and wait for the case to settle.
• Our funding eliminates the risk, hassle and uncertainty associated with PI cases.
• You get paid 100% NON-RECOURSE
• Include contact phone number (800) 472-5190
• >No Hassles
• >No Risk
• >Guaranteed Funds.
Nice to have
• Smiling doctor picture
Should not have
• Too much information

```html
<!DOCTYPE html>
<html lang="en">
<head>
<meta charset="utf-8">
<title>Personal Injury Case Funding – Qorva Financial</title>
<link rel="stylesheet" href="https://fonts.googleapis.com/css2?family=Montserrat:ital,wght@0,300;0,400;0,500;0,600;0,700;0,800;1,700;1,800&display=swap">
<style>
  :root {
    --maroon: #4e1718;
    --maroon-deep: #3f1213;
    --ink: #1f1c2b;
    --navy: #1b2236;
    --grey-text: #4a4a4a;
    --page: #e9e7e4;
    --paper: #ffffff;
    --paper-shade: #e6e6e6;
    --stamp: #c9302c;
  }
  * { margin: 0; padding: 0; box-sizing: border-box; }
  html, body {
    width: 996px; height: 1200px; overflow: hidden;
    background: var(--page);
    font-family: "Montserrat", Arial, sans-serif;
  }
  .flyer {
    position: absolute; left: 88px; top: 18px;
    width: 818px; height: 1163px;
    background: var(--paper);
    overflow: hidden;
    box-shadow: 0 2px 10px rgba(0,0,0,.15);
  }
  .photo {
    position: absolute; left: 0; top: 0; width: 818px; height: 590px;
    background:
      radial-gradient(ellipse 180px 260px at 200px 380px, #dfe6ee 0%, rgba(223,230,238,0) 100%),
      radial-gradient(ellipse 260px 200px at 420px 430px, #c9d8e8 0%, rgba(201,216,232,0) 100%),
      linear-gradient(180deg, #ffffff 0%, #f4f6f8 45%, #e3e9ef 100%);
  }
  .title-tab {
    position: absolute; left: 40px; top: 0; width: 732px; height: 118px;
    background: var(--paper);
    border-radius: 0 0 36px 36px;
    box-shadow: 0 8px 14px rgba(0,0,0,.18);
    text-align: center;
  }
  .title {
    margin-top: 26px;
    font-weight: 800; font-size: 34px; letter-spacing: .3px;
    color: var(--maroon);
  }
  .tagline {
    margin-top: 2px;
    font-weight: 800; font-style: italic; font-size: 21px;
    color: var(--maroon-deep);
  }
  .brand {
    position: absolute; right: 24px; top: 146px;
    display: flex; align-items: center;
    white-space: nowrap;
  }
  .brand-mark {
    flex: none; width: 18px; height: 18px; background: var(--maroon); margin-right: 8px;
  }
  .brand-name {
    font-weight: 700; font-size: 22px; color: var(--ink);
    padding-right: 10px; border-right: 1px solid #999;
    line-height: 50px;
  }
  .brand-sub {
    padding-left: 9px;
    font-weight: 600; font-size: 13px; line-height: 17px; color: var(--maroon);
  }
  .brand-sub span { color: #555; }
  .phone {
    position: absolute; right: 22px; top: 204px;
    font-weight: 600; font-size: 34px; color: var(--maroon-deep); letter-spacing: .5px;
    white-space: nowrap;
  }
  .promise-blob {
    position: absolute; left: 512px; top: 290px;
  }
  .promises {
    position: absolute; left: 546px; top: 340px; list-style: none;
  }
  .promises li {
    display: flex; align-items: flex-start;
    font-weight: 800; font-style: italic; font-size: 25px; line-height: 28px;
    color: var(--maroon); margin-bottom: 13px;
  }
  .promises svg { flex: none; margin: 2px 18px 0 0; }
  .how-band { position: absolute; left: 0; top: 566px; }
  .how-text {
    position: absolute; left: 0; top: 596px; width: 804px; text-align: center; color: #fff;
  }
  .how-text h2 { font-weight: 600; font-size: 32px; }
  .how-text p { font-weight: 300; font-size: 20px; margin-top: 3px; }
  .lower {
    position: absolute; left: 0; top: 690px; width: 818px; height: 473px;
    background: linear-gradient(180deg, var(--paper-shade) 0%, #f8f8f8 45%, #ffffff 100%);
  }
  .steps-head {
    position: absolute; left: 0; top: 728px; width: 790px; text-align: center;
  }
  .steps-head .big {
    font-weight: 800; font-size: 38px; color: #2b1c1c; line-height: 44px;
  }
  .steps-head .big b { font-size: 44px; color: var(--maroon); }
  .steps-head .sub {
    font-weight: 800; font-size: 22px; color: var(--navy); margin-top: 2px;
  }
  .step { position: absolute; top: 841px; width: 216px; }
  .step-top { display: flex; align-items: center; }
  .step-num {
    flex: none; width: 62px; height: 62px; border-radius: 50%;
    background: var(--maroon); color: #fff;
    font-weight: 700; font-size: 32px;
    display: flex; align-items: center; justify-content: center;
    margin-right: 10px;
  }
  .step-title { font-weight: 800; font-size: 20px; line-height: 25px; color: var(--navy); margin-top: -8px; white-space: nowrap; }
  .step-desc { width: 200px; font-size: 15.5px; line-height: 21px; color: var(--grey-text); margin: 16px 0 0 8px; }
  .step-1 { left: 67px; }
  .step-2 { left: 288px; }
  .step-3 { left: 504px; }
  .step-3 .step-desc { width: 200px; }
  .payout {
    position: absolute; left: 188px; top: 1038px; display: flex; align-items: center;
  }
  .paid-badge {
    width: 96px; height: 96px; border-radius: 50%;
    background: var(--stamp); margin-right: 20px; transform: rotate(-8deg);
  }
  .payout-text { color: var(--maroon); white-space: nowrap; }
  .payout-text .line1 { font-weight: 600; font-size: 25px; }
  .payout-text .line1 b { font-weight: 700; color: var(--maroon-deep); }
  .payout-text .line2 { font-weight: 800; font-size: 31px; line-height: 34px; }
  .payout-text .url { font-weight: 700; font-size: 19px; color: var(--navy); }
</style>
</head>
<body>
  <main class="flyer">
    <div class="photo" role="img" aria-label="Smiling female doctor with stethoscope in front of a blurred medical team"></div>

    <header class="title-tab">
      <h1 class="title">PERSONAL INJURY CASE FUNDING</h1>
      <p class="tagline">We Ensure Your Cases are Financially Sound</p>
    </header>

    <div class="brand">
      <span class="brand-mark"></span>
      <span class="brand-name">Qorva Financial</span>
      <span class="brand-sub">Receivable<br>Management<br><span>Solutions</span></span>
    </div>
    <div class="phone">(800) 472-5190</div>

    <svg class="promise-blob" width="306" height="270" viewBox="0 0 306 270" aria-hidden="true">
      <path d="M306 0 L306 270 L200 270 C90 262 12 210 2 140 C-6 70 60 8 170 2 Z" fill="#ffffff"/>
    </svg>
    <ul class="promises">
      <li><svg width="30" height="26" viewBox="0 0 30 26"><path d="M2 14 L11 23 L28 3" fill="none" stroke="#1b2236" stroke-width="5" stroke-linecap="round" stroke-linejoin="round"/></svg>NO HASSLES</li>
      <li><svg width="30" height="26" viewBox="0 0 30 26"><path d="M2 14 L11 23 L28 3" fill="none" stroke="#1b2236" stroke-width="5" stroke-linecap="round" stroke-linejoin="round"/></svg>NO RISK</li>
      <li><svg width="30" height="26" viewBox="0 0 30 26"><path d="M2 14 L11 23 L28 3" fill="none" stroke="#1b2236" stroke-width="5" stroke-linecap="round" stroke-linejoin="round"/></svg>GUARANTEED<br>FUNDS</li>
    </ul>

    <div class="lower"></div>
    <svg class="how-band" width="818" height="130" viewBox="0 0 818 130" aria-hidden="true">
      <path d="M0 4 Q409 -6 818 8 L818 112 Q409 128 0 120 Z" fill="#4e1718"/>
    </svg>
    <section class="how-text">
      <h2>How Does MVA/PI Funding Work?</h2>
      <p>We pay you upfront and wait for the case to settle.</p>
    </section>

    <section class="steps-head">
      <div class="big"><b>3</b> STEPS</div>
      <div class="sub">TO SUCCESSFUL PI CASE MANAGEMENT</div>
    </section>

    <div class="step step-1">
      <div class="step-top"><span class="step-num">1</span><span class="step-title">EVALUATE<br>CASES</span></div>
      <p class="step-desc">Evaluate the financial aspects of the case including policy limits.</p>
    </div>
    <div class="step step-2">
      <div class="step-top"><span class="step-num">2</span><span class="step-title">CONSULT<br>ATTORNEYS</span></div>
      <p class="step-desc">Evaluate the case background and<br>likelihood of settlement.</p>
    </div>
    <div class="step step-3">
      <div class="step-top"><span class="step-num">3</span><span class="step-title">GUARANTEED<br>FUNDING</span></div>
      <p class="step-desc">15 day funding on most cases.</p>
    </div>

    <footer class="payout">
      <span class="paid-badge"></span>
      <div class="payout-text">
        <div class="line1">You get paid <b>100%</b></div>
        <div class="line2">NON-RECOURSE</div>
        <div class="url">www.qorvafinancial-example.com</div>
      </div>
    </footer>
  </main>
</body>
</html>
```